Business card design for Virtual Assistance company

I need a business card designed for my virtual assistance company. We are a small company who services primarily C-level executive clients. The card needs to be double sided with the following contact information on the back:
Melanie Hartwick
Owner/CEO
info@pbtadvisory.net
www.pbtadvisory.net
240.395.2817

The front side should just have the company name incorporated: "PBT Advisory" and "virtual assistance"

The card should be simplistic, but eye catching and should speak to high level executives. Our primary focus areas consist of executive assistance and government contracting.

Target Market(s)

CEOs and executives

Contact Information for Business Card

see project description. phone, email, website.

Colors

Designer to choose only greyscale colors for use in the design.

```html
<!DOCTYPE html>
<html lang="en">
<head>
<meta charset="utf-8">
<title>PBT Advisory – Business Card</title>
<link href="https://fonts.googleapis.com/css2?family=Inter:wght@400;700;800&display=swap" rel="stylesheet">
<style>
  :root {
    --backdrop: #2b2b2b;
    --card: #141414;
    --ink-light: #e8e8e8;
    --ink-muted: #8a8a8a;
    --accent: #2a9fd8;
    --shadow: rgba(0, 0, 0, 0.55);
  }
  * { margin: 0; padding: 0; box-sizing: border-box; }
  html, body {
    width: 1200px;
    height: 689px;
    overflow: hidden;
    background: var(--backdrop);
    font-family: "Inter", Arial, sans-serif;
  }
  .stage {
    position: relative;
    width: 1200px;
    height: 689px;
    display: flex;
    align-items: center;
    justify-content: center;
    gap: 40px;
  }
  .card {
    position: relative;
    width: 540px;
    height: 309px;
    background: var(--card);
    box-shadow: 0 18px 40px var(--shadow);
  }

  /* Front side */
  .card-front {
    display: flex;
    flex-direction: column;
    justify-content: center;
    padding-left: 56px;
  }
  .company-name {
    font-weight: 800;
    font-size: 50px;
    letter-spacing: -0.5px;
    line-height: 1;
    color: var(--ink-light);
  }
  .company-tagline {
    margin-top: 10px;
    font-weight: 800;
    font-size: 42px;
    letter-spacing: -0.5px;
    line-height: 1;
    color: var(--ink-muted);
  }

  /* Back side */
  .card-back {
    display: flex;
    align-items: center;
    padding-left: 48px;
  }
  .person {
    text-align: right;
    padding-top: 34px;
  }
  .person-name {
    font-weight: 700;
    font-size: 30px;
    letter-spacing: 0.3px;
    color: var(--accent);
    line-height: 1.05;
  }
  .person-title {
    font-weight: 400;
    font-size: 15px;
    color: var(--ink-light);
    margin-top: 2px;
  }
  .divider {
    width: 1.5px;
    height: 78px;
    background: var(--accent);
    margin: 0 16px 0 18px;
  }
  .contact-list {
    list-style: none;
    display: flex;
    flex-direction: column;
    gap: 6px;
  }
  .contact-item {
    display: flex;
    align-items: center;
    gap: 7px;
    font-size: 14px;
    color: var(--ink-light);
    letter-spacing: 0.2px;
  }
  .contact-icon {
    width: 12px;
    height: 12px;
    fill: var(--accent);
    flex: none;
  }
</style>
</head>
<body>
<main class="stage">
  <section class="card card-front" aria-label="Card front">
    <h1 class="company-name">PBT Advisory</h1>
    <p class="company-tagline">Virtual Assistance</p>
  </section>

  <section class="card card-back" aria-label="Card back">
    <div class="person">
      <p class="person-name">Melanie Hartwick</p>
      <p class="person-title">Owner/CEO</p>
    </div>
    <span class="divider"></span>
    <ul class="contact-list">
      <li class="contact-item">
        <svg class="contact-icon" viewBox="0 0 12 12" aria-hidden="true">
          <path d="M1 4.5C1 3 3 2 6 2s5 1 5 2.5V5.5H8.5V4.3C7.8 4 6.9 3.9 6 3.9S4.2 4 3.5 4.3V5.5H1Z"/>
          <path d="M3.2 6h5.6l1.7 4.5H1.5Z"/>
        </svg>
        <span>240.395.2817</span>
      </li>
      <li class="contact-item">
        <svg class="contact-icon" viewBox="0 0 12 12" aria-hidden="true">
          <path d="M1 2.5h10v1L6 6.8 1 3.5Z"/>
          <path d="M1 4.8 6 8l5-3.2V9.5H1Z"/>
        </svg>
        <span>info@pbtadvisory.net</span>
      </li>
      <li class="contact-item">
        <svg class="contact-icon" viewBox="0 0 12 12" aria-hidden="true">
          <circle cx="6" cy="6" r="5"/>
          <path d="M3.4 3.5c1 .2 1.6.9 1.4 1.8-.2.8.8 1.2.6 2.2L4.8 9.5C3.4 8.3 2.6 6.6 2.8 4.6Z" fill="var(--card)"/>
          <path d="M7 2.2c.6.8 1.8.6 2.3 1.6-.5.6-1.5.4-2 1.2-.4.7.5 1.4 1.4 1.5C8.5 7.5 8 8.4 7.4 9 7 7.8 6 7.3 6.4 6.1 5.6 5 6.5 3 7 2.2Z" fill="var(--card)"/>
        </svg>
        <span>www.pbtadvisory.net</span>
      </li>
    </ul>
  </section>
</main>
</body>
</html>
```